依頼詳細
制作目的
講座の参加者を募集するため。

用途
自然學校HPにPDFを掲載。また、講師など関係者を通じてその所属大学や近隣の大学に配布。チラシに掲載したQRコードを読み取り、申込フォームから申し込んでもらう。

ターゲット
学生(大学生や専門学生、短大生など)20名
特に、SDGsに興味関心があり、学びや対話に意欲的な方。社会課題に対して意識が高く、自身でも何かアクションを起こしたいと考えている方の参加を期待します。
記載項目
記載原稿については添付ファイルをご確認ください。
使用画像については、下記URLよりダウンロードをお願いいたします。
(写真タイトルに回数が入っているものもありますが、デザインにより配置等はお任せしますのでご参考まで。)
https://31.hakobune-dl.net/0907-3d1b8e02a7c4f9d6e5b0a1c28f7e4d93

画像について、当星苑塾舎のHPや活動記録(mosa)等で掲載している写真を使っていただいても構いません。元データをお送りすることも可能ですのでお申し付けください。また追加で必要な画像等がありましたらご相談ください。

表面:講座名/キャッチコピー/メイン写真(活動風景写真から選出)/サブ写真(白川郷)/イベント概要と趣旨/日程/参加費/定員/会場/対象/主催者/後援
裏面:講座名/日程と講座の詳細/滞在イメージ写真/活動風景写真/会場アクセス/申込方法/施設ロゴ
サイズ
A4
ページ数
両面
希望イメージ
シンプル 複雑
単色 カラフル
暗い 明るい
日常 高級
遊び心 厳粛
未来的 伝統的
女性的 男性的
希望する色
設定なし
納品ファイル
• イラストレーター形式 (.ai)
補足説明
イラストレーター形式及び高解像度PDFでも納品をお願いしたいです。ネット印刷を予定しております。

表面の良く目立つタイトルと、全4回の活動と季節感のある写真配置が良く、また裏面の見やすさから、こちらを選定させていただきました。

短い期間にもかかわらず、たくさんのご提案をいただきましてありがとうございました。またの機会がございましたら、ご提案いただければ幸いです。この度は誠にありがとうございました。

```html
<!DOCTYPE html>
<html lang="ja">
<head>
<meta charset="utf-8">
<title>SDGs 担い手育成講座</title>
<link rel="stylesheet" href="https://fonts.googleapis.com/css2?family=Noto+Sans+JP:wght@400;500;700;900&family=Noto+Serif+JP:wght@700;900&display=swap">
<style>
:root{
  --ink:#2b2b2b;
  --sub:#555;
  --line:#d8d3c8;
  --paper:#ffffff;
  --c1:#e2574c;
  --c2:#f08a24;
  --c3:#2f8fc4;
  --c4:#4aa35a;
  --c1-soft:#fdeeec;
  --c2-soft:#fef3e6;
  --c3-soft:#eaf4fa;
  --c4-soft:#ecf6ee;
}
*{box-sizing:border-box;margin:0;padding:0}
html,body{width:849px;height:1200px;overflow:hidden;background:var(--paper)}
body{font-family:"Noto Sans JP",sans-serif;color:var(--ink);position:relative}
.photo{position:absolute;border-radius:2px}
.hero{position:absolute;left:0;top:0;width:849px;height:250px}
.course-title{position:absolute;left:0;top:262px;width:849px;text-align:center;font-family:"Noto Serif JP",serif;font-size:46px;font-weight:900;letter-spacing:2px;line-height:60px}
.course-title .en{margin-right:14px}
.wanted{position:absolute;left:30px;top:332px;width:789px;display:flex;gap:14px;align-items:center}
.wanted-label{flex:none;font-size:12px;font-weight:700;line-height:1.35;color:var(--c1);border:1.5px solid var(--c1);padding:3px 8px;border-radius:3px}
.wanted-list{list-style:none;font-size:10.5px;line-height:1.7;color:var(--sub)}
.sessions{position:absolute;left:30px;top:382px;width:789px;display:grid;grid-template-columns:1fr 1fr;gap:12px 18px}
.session{border:1.5px solid var(--accent);border-radius:6px;height:172px;padding:9px 12px;background:var(--soft)}
.session-head{display:flex;align-items:center;gap:8px;height:22px}
.session-no{background:var(--accent);color:#fff;font-weight:700;font-size:13px;padding:1px 8px;border-radius:3px}
.session-date{color:var(--accent);font-weight:700;font-size:16px}
.session-date b{font-size:11px;margin-right:4px}
.session-theme{margin-top:6px;font-size:15px;font-weight:900;background:#fff;border-left:4px solid var(--accent);padding:3px 8px;line-height:22px}
.session-lead{font-size:9.5px;margin-top:5px;color:var(--sub);line-height:1.45;white-space:nowrap}
.program{margin-top:5px;font-size:10px;line-height:16px}
.program dt{float:left;clear:left;width:104px;color:var(--accent);font-weight:700;white-space:nowrap}
.program dt::before{content:"■";margin-right:3px}
.program dd{margin-left:104px}
.s1{--accent:var(--c1);--soft:var(--c1-soft)}
.s2{--accent:var(--c2);--soft:var(--c2-soft)}
.s3{--accent:var(--c3);--soft:var(--c3-soft)}
.s4{--accent:var(--c4);--soft:var(--c4-soft)}
.info{position:absolute;left:30px;top:748px;width:380px;font-size:10.5px;line-height:1.6}
.info h3{font-size:12px;font-weight:700;margin-top:6px}
.info h3:first-of-type{margin-top:0}
.info h3::before{content:"■";color:var(--c3);margin-right:3px}
.info p{color:var(--sub)}
.qr-spot{width:58px;height:58px;border:1.5px solid var(--ink);float:right;margin:2px 0 0 10px;background:#fff}
.map{position:absolute;left:430px;top:748px;width:389px;height:262px;border:1px solid var(--line);background:linear-gradient(160deg,#f3f0e6,#e6ecdf 60%,#dfe8ef)}
.room{position:absolute;top:1030px;height:140px;border-radius:2px}
.brand{position:absolute;left:430px;top:1030px;display:flex;align-items:center;gap:8px;font-size:18px;font-weight:700}
.brand i{width:16px;height:16px;background:var(--c4);display:block}
.site-url{position:absolute;left:430px;top:1070px;font-size:25px;font-weight:700;letter-spacing:.3px;white-space:nowrap}
</style>
</head>
<body>
<div class="hero">
  <div class="photo" role="img" aria-label="白川郷の合掌造り集落の風景写真" style="left:0;top:0;width:230px;height:250px;background:linear-gradient(180deg,#a8c2d6,#6f8a5a)"></div>
  <div class="photo" role="img" aria-label="講座で学生が対話する様子の写真" style="left:234px;top:0;width:150px;height:123px;background:linear-gradient(135deg,#d9cdb6,#9c8a6c)"></div>
  <div class="photo" role="img" aria-label="森の中でのフィールドワークの写真" style="left:234px;top:127px;width:150px;height:123px;background:linear-gradient(135deg,#90a874,#51693f)"></div>
  <div class="photo" role="img" aria-label="雪の集落を歩く参加者の写真" style="left:388px;top:0;width:200px;height:250px;background:linear-gradient(180deg,#e8eef2,#b3c0c9)"></div>
  <div class="photo" role="img" aria-label="室内でのレクチャーの写真" style="left:592px;top:0;width:257px;height:123px;background:linear-gradient(135deg,#d7b98c,#9a7a52)"></div>
  <div class="photo" role="img" aria-label="茅葺き屋根の前で作業する参加者の写真" style="left:592px;top:127px;width:257px;height:123px;background:linear-gradient(135deg,#b9c39a,#6f7d4e)"></div>
</div>

<h1 class="course-title"><span class="en">SDGs</span>担い手育成講座</h1>

<div class="wanted">
  <div class="wanted-label">こんな人を<br>募集します</div>
  <ul class="wanted-list">
    <li>●SDGsに興味関心がある　●社会課題に対して何かアクションを起こしたい</li>
    <li>●未来の社会について考えて動きたい　●語り合える仲間とつながりたい</li>
  </ul>
</div>

<section class="sessions">
  <article class="session s1">
    <div class="session-head"><span class="session-no">第1回</span><span class="session-date"><b>2023</b>7/7(金)〜9(日)</span></div>
    <h2 class="session-theme">「SDGsって?白川郷って?」</h2>
    <p class="session-lead">SDGs担い手にとって必要な“視点”と“問い”を得る</p>
    <dl class="program">
      <dt>レクチャー</dt><dd>里の暮らしと未来へ送る力</dd>
      <dt>フィールドワーク</dt><dd>世界遺産集落 景観保全体験</dd>
      <dt>対話</dt><dd>サステナビリティとは?</dd>
      <dt>交流</dt><dd>学生間交流</dd>
    </dl>
  </article>
  <article class="session s2">
    <div class="session-head"><span class="session-no">第2回</span><span class="session-date"><b>2023</b>10/20(金)〜22(日)</span></div>
    <h2 class="session-theme">「白川郷って意外とサステナブル」</h2>
    <p class="session-lead">なぜ、続いてきたのかを考える</p>
    <dl class="program">
      <dt>レクチャー</dt><dd>合掌造り集落の保存と暮らしの知恵</dd>
      <dt>フィールドワーク</dt><dd>森と水の循環を歩く</dd>
      <dt>対話</dt><dd>持続してきた理由を探る</dd>
      <dt>交流</dt><dd>村民との交流</dd>
    </dl>
  </article>
  <article class="session s3">
    <div class="session-head"><span class="session-no">第3回</span><span class="session-date"><b>2023</b>12/15(金)〜17(日)</span></div>
    <h2 class="session-theme">「社会と子どもたちの声を聴く」</h2>
    <p class="session-lead">未来に目を向け、持続可能な未来のために活動してきた人の事例を知る</p>
    <dl class="program">
      <dt>レクチャー</dt><dd>持続可能な未来のためにできること</dd>
      <dt>フィールドワーク</dt><dd>冬の集落と暮らしの見学</dd>
      <dt>対話</dt><dd>子どもたちの声から考える</dd>
      <dt>交流</dt><dd>未来の担い手との交流</dd>
    </dl>
  </article>
  <article class="session s4">
    <div class="session-head"><span class="session-no">第4回</span><span class="session-date"><b>2024</b>2/23(金)〜25(日)</span></div>
    <h2 class="session-theme">「将来の自分と社会の未来を考える」</h2>
    <p class="session-lead">持続可能な未来のためにできることを考え、自分ができることをみつける</p>
    <dl class="program">
      <dt>レクチャー</dt><dd>SDGsを体験する</dd>
      <dt>フィールドワーク</dt><dd>雪国の暮らし体験</dd>
      <dt>対話</dt><dd>自分のアクションを語る</dd>
      <dt>交流</dt><dd>未来の担い手同士の交流</dd>
    </dl>
  </article>
</section>

<section class="info">
  <div class="qr-spot" aria-label="申込フォームのQRコード"></div>
  <h3>お申し込み方法</h3>
  <p>詳細は下記よりご確認ください。<br>https://seien-juku.example.jp/news/<br>右のQRコードの申込フォームからお申し込みください。</p>
  <h3>締切</h3>
  <p>2023年5月31日(水)までにお申し込みください。<br>※定員になり次第締め切ります。</p>
  <h3>対象</h3>
  <p>学生(大学生、専門学生、短大生 等)</p>
  <h3>お問い合わせ</h3>
  <p>星苑塾舎<br>〒501-0000 岐阜県星苑郡森見村字苑台12<br>TEL.0000-12-3456　Mail. info@seien-juku.example.jp</p>
</section>

<div class="map" role="img" aria-label="会場までのアクセス地図(周辺の高速道路と主要都市からの経路)"></div>

<div class="room" role="img" aria-label="宿泊施設の客室の写真" style="left:30px;width:186px;background:linear-gradient(135deg,#c9a97e,#8f6b45)"></div>
<div class="room" role="img" aria-label="施設での食事の写真" style="left:224px;width:186px;background:linear-gradient(135deg,#e2d2b8,#a88a62)"></div>

<div class="brand"><i></i>星苑塾舎</div>
<div class="site-url">https://seien-juku.example.jp</div>
</body>
</html>
```